Medical Centre Website

We need a new design for a medical centre based in Perth, Western Australia called 'Tarwick Valley Medical Centre'.

The medical centre does general practitioner work including general checkups, ecg, heart checks, woman's health and more servicing children and adults. They also do home visits on occasions where the patient cannot attend the centre.

They would like an information/brochure website where visitors can read up on the practice, send email and view their location.

The client wish the design to be clean, fresh and light. The main colours are a light purple/blue and to a dark navy blue. The client would not want the logo to be altered in any way. This includes changing the words colours or the image.

The final design should represent a loving, family friendly practice where patients can come to receive the best treatments.

We just need the end product to be presented to un in a layed psd format. The fonts must be as per the W3C standards.

**IMPORTANT**
I have received heaps of skype invites in the past. To treat everyone fairly, I do not add people to my skype list as in the past people expected us to give them the prize. If you have questions, please ask them in pixel forum as it may benefit others who are also designing the site. If I need to, I will send a message to the user.
Updates

Hi Designers,

Most designs we have received have been overly cluttered. Are you able to simplify the designs.

Cheers, Dorian

Hi Designers,

Some of the designs are quite attractive but aremore cluttered than I would like. If you have a look at the following design, the design is very simple and straight to the point. A lot of designs have too much wording and the reader can be put off. We are looking something more like:

fernoakclinic.com.au

I would prefer to see designs and have opened up the contest for a further 7 days.

Designers,

We have received feedback from the client and Quite frankly he don’t really like any of them.They are too cluttered and Americanised. All drab blue colours.
 
If you have a look at template monster, these designs are better and cleaner. We do not want heaps of writing on the front page.

If you look at the eariler examples such as kelbrookgp.com.au which I did myself, the client loves that simplicity of the site.

```html
<!DOCTYPE html>
<html lang="en">
<head>
<meta charset="utf-8">
<title>Tarwick Valley Medical Centre</title>
<link rel="stylesheet" href="https://fonts.googleapis.com/css2?family=Open+Sans:wght@300;400;600;700&display=swap">
<style>
:root{
  --blue:#1a5fb0;
  --lilac:#98aad6;
  --ink:#333;
  --muted:#777;
  --line:#e2e2e2;
  --hero-dark:#0b3a96;
  --hero-light:#2a66c6;
}
*{box-sizing:border-box;margin:0;padding:0}
html,body{width:1200px;height:1138px;overflow:hidden}
body{
  position:relative;font-family:"Open Sans",sans-serif;color:var(--ink);
  background:linear-gradient(160deg,#e9eef9 0%,#f7f9fd 30%,#dde6f6 60%,#f3f6fc 80%,#d9e2f4 100%);
}
.page{position:absolute;left:100px;top:20px;width:1000px;height:850px;background:#fff;box-shadow:0 0 6px rgba(0,0,0,.18)}
.brand{position:absolute;display:flex;align-items:center;gap:10px;color:var(--blue);font-weight:400;white-space:nowrap}
.brand .mark{width:14px;height:14px;border-radius:50%;background:var(--lilac)}
.brand-header{left:20px;top:50px;font-size:24px}
.call{position:absolute;right:20px;top:36px;text-align:right}
.call-label{font-size:16px;color:#444;display:flex;align-items:center;justify-content:flex-end;gap:6px}
.call-number{font-size:26px;font-weight:300;color:var(--blue);line-height:34px}
.nav{position:absolute;left:10px;top:118px;width:979px;height:40px;display:flex;list-style:none;background:linear-gradient(#fff,#ececec);border-top:1px solid var(--line)}
.nav li{height:40px;display:flex;align-items:center;justify-content:center;font-size:16px;color:var(--blue);border-left:1px solid #e4e4e4}
.nav li.active{background:var(--lilac);color:#1b2a4a;border-left:none}
.hero{position:absolute;left:10px;top:168px;width:980px;height:342px;border:3px solid #444;background:linear-gradient(100deg,var(--hero-dark) 0%,var(--hero-light) 55%,#c9ccd2 75%,#e4e2dc 100%)}
.hero-title{position:absolute;left:13px;top:78px;width:360px;font-size:30px;font-weight:300;line-height:32px;color:#fff}
.hero-btn{position:absolute;left:14px;top:184px;width:90px;height:35px;background:#fff;font-size:16px;color:#333;display:flex;align-items:center;justify-content:center}
.dots{position:absolute;right:6px;bottom:8px;display:flex;gap:5px}
.dots span{width:10px;height:10px;border-radius:50%;background:rgba(255,255,255,.45)}
.dots span:first-child{background:#fff}
.welcome{position:absolute;left:20px;top:530px;width:620px}
h1,h2{font-weight:300;color:var(--blue)}
.welcome h1{font-size:26px;line-height:34px;margin-bottom:4px}
.welcome p{font-size:12.5px;line-height:18px;margin-bottom:18px}
.btn-more{position:absolute;left:20px;top:795px;width:90px;height:33px;border:1px solid #bbb;border-radius:2px;background:linear-gradient(#fafafa,#dcdcdc);font-size:12px;font-weight:700;color:#222;display:flex;align-items:center;justify-content:center}
.appoint{position:absolute;left:680px;top:536px;width:300px}
.appoint h2{font-size:20px;line-height:28px;margin-bottom:6px}
.appoint p{font-size:12.5px;line-height:19px;padding-left:2px}
.contact-box{position:absolute;left:682px;top:643px;width:297px;height:103px;border:1px solid #ddd;border-radius:3px;background:#fafafa;padding:0 10px}
.contact-row{height:51px;display:flex;align-items:center;gap:8px;border-bottom:1px solid var(--line)}
.contact-row:last-child{border-bottom:none}
.contact-row em{font-size:12.5px;color:#999;font-style:italic}
.contact-row .big{font-size:19px;font-weight:600;color:#333}
.contact-row .mid{font-size:15px;font-weight:600;color:#333}
.fill-note{position:absolute;left:682px;top:759px;font-size:12.5px}
.btn-form{position:absolute;left:682px;top:794px;width:170px;height:34px;background:var(--lilac);border:1px solid #7e92c6;border-radius:2px;color:#fff;font-size:12px;font-weight:700;display:flex;align-items:center;padding-left:9px;gap:22px}
.btn-form i{display:block;width:1px;height:34px;background:#b8c4e4}
.footer-col{position:absolute;top:905px}
.footer-col h3{font-size:15px;font-weight:700;color:var(--blue);line-height:22px;margin-bottom:10px}
.footer-col li{list-style:none;font-size:12px;line-height:23px;color:#333}
.social{display:flex;gap:16px;margin-top:4px}
.social span{width:20px;height:20px;border-radius:50%;background:#8b97ad}
.brand-footer{left:0;top:94px;font-size:20px}
.copy{position:absolute;left:100px;top:1101px;font-size:12px}
</style>
</head>
<body>
<div class="page">
  <div class="brand brand-header"><span class="mark"></span>Tarwick Valley Medical Centre</div>
  <div class="call">
    <div class="call-label">
      <svg width="14" height="14" viewBox="0 0 14 14"><path d="M3 1l2 3-1.3 1.3a8 8 0 0 0 5 5L10 9l3 2-1 2C6 13 1 8 1 2z" fill="#333"/></svg>
      Call us Directly:
    </div>
    <div class="call-number">1800 317 2208</div>
  </div>
  <ul class="nav">
    <li class="active" style="width:157px">Home</li>
    <li style="width:167px">About Us</li>
    <li style="width:166px">Medical Services</li>
    <li style="width:166px">Appointments</li>
    <li style="width:166px">Our Doctors</li>
    <li style="width:157px">Location</li>
  </ul>
  <div class="hero" role="img" aria-label="Photo of a hospital building with emergency and main entrance signs against a blue sky">
    <div class="hero-title">Expert Care from the most minor to the most serious cases</div>
    <div class="hero-btn">Read More</div>
    <div class="dots"><span></span><span></span><span></span><span></span></div>
  </div>
  <section class="welcome">
    <h1>Welcome to Tarwick Valley Medical Centre</h1>
    <p>On sait depuis longtemps que travailler avec du texte lisible et contenant du sens est source de distractions, et empêche de se concentrer sur la mise en page elle-même. L'avantage du Lorem Ipsum sur un texte générique comme 'Du texte. Du texte.</p>
    <p>Du texte.' est qu'il possède une distribution de lettres plus ou moins normale, et en tout cas comparable avec celle du français standard.De nombreuses suites logicielles de mise en page ou éditeurs de sites Web ont fait du Lorem Ipsum leur faux texte par défaut, et une recherche pour 'Lorem Ipsum' vous conduira vers de nombreux sites qui n'en sont encore qu'à leur phase de construction. Plusieurs versions sont apparues avec le temps, parfois par accident.rd.De nombreuses suites logicielles de mise en page ou éditeurs de sites Web ont fait du Lorem Ipsum leur faux texte par défaut, et une recherche pour 'Lorem Ipsum' vous conduira vers de nombreux sites qui n'en sont encore qu'à leur phase de construction. Plusieurs versions sont apparues avec le temps, parfois par accident.</p>
  </section>
  <div class="btn-more">READ MORE</div>
  <section class="appoint">
    <h2>Make an Appointment</h2>
    <p>Le Lorem Ipsum est simplement du faux texte em-ployé dans la composition et la mise en page avant impression.</p>
  </section>
  <div class="contact-box">
    <div class="contact-row">
      <svg width="12" height="12" viewBox="0 0 14 14"><path d="M3 1l2 3-1.3 1.3a8 8 0 0 0 5 5L10 9l3 2-1 2C6 13 1 8 1 2z" fill="#bbb"/></svg>
      <em>by Phone:</em><span class="big">+61 (0) 8 9320 4471</span>
    </div>
    <div class="contact-row">
      <svg width="13" height="10" viewBox="0 0 13 10"><rect x=".5" y=".5" width="12" height="9" fill="none" stroke="#bbb"/><path d="M.5 .5l6 5 6-5" fill="none" stroke="#bbb"/></svg>
      <em>by Email:</em><span class="mid">bookings@tarwickvalley.com.au</span>
    </div>
  </div>
  <div class="fill-note">... or fill in the form on our Appointments page:</div>
  <div class="btn-form">FILL IN THE FORM<i></i>
    <svg width="14" height="14" viewBox="0 0 14 14"><rect x="1" y="3" width="10" height="10" fill="none" stroke="#fff" stroke-width="1.5"/><path d="M6 8l6-6" stroke="#fff" stroke-width="2"/></svg>
  </div>
</div>

<div class="footer-col" style="left:100px"><h3>Adipisicing elit</h3><ul><li>L'extrait standard</li><li>Utilisé depuis</li><li>XVIè siècle est</li><li>Reproduit</li><li>Dessous pour</li><li>Curieux les sections</li></ul></div>
<div class="footer-col" style="left:295px"><h3>Pendant la</h3><ul><li>L'extrait standard</li><li>Utilisé depuis</li><li>XVIè siècle est</li><li>Reproduit</li></ul></div>
<div class="footer-col" style="left:491px"><h3>Pour Générer</h3><ul><li>L'extrait standard</li><li>Utilisé depuis</li><li>XVIè siècle est</li><li>Reproduit</li><li>Dessous pour</li></ul></div>
<div class="footer-col" style="left:686px"><h3>Structures</h3><ul><li>L'extrait standard</li><li>Utilisé depuis</li><li>XVIè siècle est</li><li>Reproduit</li><li>Dessous pour</li><li>Curieux les sections</li></ul></div>
<div class="footer-col" style="left:859px;width:241px">
  <h3>Follow Us</h3>
  <div class="social"><span></span><span></span><span></span><span></span></div>
  <div class="brand brand-footer"><span class="mark"></span>Tarwick Valley</div>
</div>
<div class="copy">© Copyrights 2013 All rights Reserved</div>
</body>
</html>
```